Loom Haven needs a website

I sell rugs and carpet on my website, loomhavenfloors.example. I need help with the site design to make it "pop". The logo in the header has been designed and I want the site to match it's style and color. Also I have some example sites for layout:
matvale.example
weave-outlet.example

Industry/Entity Type

Carpet

Requirements
Must have
• Scrolling images on front page. I will insert photos, just need the code.

```html
<!DOCTYPE html>
<html lang="en">
<head>
<meta charset="utf-8">
<title>Loom Haven — Rugs &amp; Carpet</title>
<link href="https://fonts.googleapis.com/css2?family=Questrial&display=swap" rel="stylesheet">
<style>
:root{
  --green:#7cc576;
  --navy:#123a63;
  --black:#111;
  --ink:#2b2b2b;
  --wood-a:#8a6a48;
  --wood-b:#a0805c;
  --footer:#efefef;
  --line:#e2e2e2;
  --white:#fff;
}
*{margin:0;padding:0;box-sizing:border-box}
html,body{width:734px;height:1200px;overflow:hidden;background:var(--white)}
body{position:relative;font-family:"Questrial",sans-serif;color:var(--ink)}
.abs{position:absolute}
.wood{left:0;top:0;width:734px;height:362px;background:linear-gradient(90deg,var(--wood-a),var(--wood-b) 30%,var(--wood-a) 55%,var(--wood-b) 80%,var(--wood-a))}
.util-links{left:90px;top:16px;font-size:8px;color:var(--white)}
.search{left:364px;top:13px;width:164px;height:22px;background:var(--white);font-size:7px;color:#888;padding:7px 6px}
.search-btn{left:528px;top:13px;width:52px;height:22px;background:var(--navy);color:var(--white);font-size:8px;text-align:center;line-height:22px}
.login-btn{left:582px;top:13px;width:61px;height:22px;background:var(--black);color:var(--white);font-size:8px;text-align:center;line-height:22px}
.header{left:90px;top:38px;width:554px;height:61px;background:var(--white);border-top:4px solid var(--green)}
.brand{left:8px;top:16px;display:flex;align-items:center;gap:6px;font-size:13px;color:var(--ink)}
.brand-mark{width:10px;height:10px;background:var(--green)}
.nav{right:18px;top:24px;display:flex;gap:20px;font-size:9px;color:var(--ink)}
.nav .current{color:var(--green)}
.hero{left:90px;top:99px;width:554px;height:234px;overflow:hidden}
.hero-photo{left:0;top:0;width:554px;height:234px;background:linear-gradient(180deg,#e4e4e2 0%,#cfcfcc 55%,#bdbdb9 100%)}
.hero-shape{left:0;top:0}
.hero-title{left:395px;top:44px;font-size:27px;line-height:25px;color:var(--white)}
.hero-offer{left:470px;top:124px;font-size:21px;line-height:19px;color:var(--white);text-align:right}
.hero-sub{left:358px;top:152px;font-size:17px;color:var(--ink)}
.hero-btn{left:356px;top:178px;width:98px;height:24px;background:var(--navy);color:var(--white);font-size:8px;text-align:center;line-height:24px}
.dots{left:10px;top:219px;display:flex;gap:5px}
.dots span{width:7px;height:7px;background:var(--navy)}
.dots span:first-child{background:var(--white)}
.special{top:374px;height:93px}
.special-img{width:100%;height:100%}
.special-cap{left:0;bottom:0;width:100%;height:26px;background:rgba(0,0,0,.8);color:var(--white);font-size:9px;text-align:center;line-height:26px}
.special-name{top:474px;font-size:8px;color:var(--black)}
.btn-green{background:var(--green);color:var(--white);font-size:7px;text-align:center}
.special-more{top:473px;width:51px;height:17px;line-height:17px}
.section-title{top:527px;font-size:11px;color:var(--black);padding-bottom:8px;border-bottom:1px solid var(--line)}
.cat-active{left:90px;top:562px;width:132px;height:100px;background:var(--green)}
.cat-active .pointer{left:132px;top:44px;width:0;height:0;border-top:6px solid transparent;border-bottom:6px solid transparent;border-left:8px solid var(--green)}
.cat-img{left:10px;top:15px;width:114px;height:61px;background:linear-gradient(135deg,#8c8a78,#6d6e62)}
.cat-label{left:10px;top:84px;font-size:8px;color:var(--white)}
.cat{left:90px;width:132px;height:32px;background:var(--green);color:var(--white);font-size:8px;padding-left:10px;line-height:32px}
.cat::after{content:"›";position:absolute;right:10px;font-size:13px}
.prod-img{width:118px;height:103px}
.prod-info{width:130px;font-size:7.5px;line-height:11px;color:var(--black)}
.prod-info b{font-weight:400;font-size:8px}
.add-btn{width:50px;height:16px;background:var(--navy);color:var(--white);font-size:6.5px;text-align:center;line-height:16px}
.more-btn{width:50px;height:16px;line-height:16px;font-size:6.5px}
.view-more{left:359px;top:969px;width:127px;height:27px;line-height:27px;font-size:8px}
.footer{left:0;top:1014px;width:734px;height:186px;background:var(--footer)}
.foot-col{top:40px;font-size:7.5px;line-height:17px;color:var(--ink)}
.subscribe{left:432px;top:41px;width:190px;height:21px;background:var(--white);border:1px solid var(--line);font-size:7.5px;padding:5px 5px}
.subscribe-btn{left:138px;top:2px;width:48px;height:15px;background:var(--navy);color:var(--white);font-size:7px;text-align:center;line-height:15px}
.social{left:542px;top:81px;display:flex;gap:3px}
.social span{width:18px;height:18px;border-radius:50%}
.copy{left:0;top:154px;width:734px;text-align:center;font-size:7.5px;color:var(--ink)}
</style>
</head>
<body>
  <div class="abs wood" role="img" aria-label="Wood grain background texture"></div>
  <div class="abs util-links">My Account &nbsp;| &nbsp;View Cart | Checkout</div>
  <div class="abs search">Search Your Product</div>
  <div class="abs search-btn">Search</div>
  <div class="abs login-btn">Login</div>

  <header class="abs header">
    <div class="abs brand"><span class="brand-mark"></span>Loom Haven</div>
    <nav class="abs nav"><span class="current">Home</span><span>About Us</span><span>Contact Us</span></nav>
  </header>

  <section class="abs hero">
    <div class="abs hero-photo" role="img" aria-label="Bright living room with white sofa, potted palm and shaggy area rug"></div>
    <svg class="abs hero-shape" width="554" height="234" viewBox="0 0 692 292" preserveAspectRatio="none">
      <polygon points="445,108 415,200 432,280 682,282" fill="#fff"/>
      <polygon points="467,24 680,24 682,282 445,108" fill="#7cc576"/>
      <path d="M560 160 A58 58 0 1 1 608 236" fill="none" stroke="#fff" stroke-width="3"/>
    </svg>
    <div class="abs hero-title">Loom<br>Haven</div>
    <div class="abs hero-offer">15 %<br>Flat</div>
    <div class="abs hero-sub">Area Rugs</div>
    <div class="abs hero-btn">View Collections</div>
    <div class="abs dots"><span></span><span></span><span></span><span></span></div>
  </section>

  <div class="abs special" style="left:90px;width:172px">
    <div class="special-img" role="img" aria-label="Brown rug with cream leaf pattern" style="background:linear-gradient(135deg,#7d7160,#a99b80,#6f6454)"></div>
    <div class="abs special-cap">Todays Special</div>
  </div>
  <div class="abs special-name" style="left:90px">Northern Birch</div>
  <div class="abs btn-green special-more" style="left:208px">More Info</div>

  <div class="abs special" style="left:275px;width:176px">
    <div class="special-img" role="img" aria-label="Red oriental rug with ornate border" style="background:linear-gradient(135deg,#5e2a22,#8a3a30,#5a2a24)"></div>
    <div class="abs special-cap">Todays Special</div>
  </div>
  <div class="abs special-name" style="left:279px">Northern Birch</div>
  <div class="abs btn-green special-more" style="left:396px">More Info</div>

  <div class="abs special" style="left:467px;width:177px">
    <div class="special-img" role="img" aria-label="Blue and grey woven carpet" style="background:linear-gradient(135deg,#4d5d6a,#6b7a7c,#465560)"></div>
    <div class="abs special-cap">Todays Special</div>
  </div>
  <div class="abs special-name" style="left:467px">Northern Birch</div>
  <div class="abs btn-green special-more" style="left:592px">More Info</div>

  <h2 class="abs section-title" style="left:90px;width:132px;font-weight:400">SHOP CATEGORY</h2>
  <h2 class="abs section-title" style="left:235px;width:409px;font-weight:400">OUR PRODUCTS</h2>

  <div class="abs cat-active">
    <div class="abs cat-img" role="img" aria-label="Commercial flooring sample"></div>
    <div class="abs cat-label">Commercial Flooring</div>
    <div class="abs pointer"></div>
  </div>
  <div class="abs cat" style="top:670px">Carpet Flooring</div>
  <div class="abs cat" style="top:707px">Harwood Flooring</div>
  <div class="abs cat" style="top:745px">Area Rugs</div>

  <!-- product row 1 -->
  <div class="abs prod-img" style="left:236px;top:562px;background:linear-gradient(135deg,#6f7a6e,#9a9478,#5f6b66)" role="img" aria-label="Patterned green and tan carpet sample"></div>
  <div class="abs prod-img" style="left:380px;top:562px;background:linear-gradient(135deg,#6c6d70,#88898c,#67686b)" role="img" aria-label="Grey carpet sample"></div>
  <div class="abs prod-img" style="left:525px;top:562px;background:linear-gradient(135deg,#8f9a36,#a8ae46,#7f8a2e)" role="img" aria-label="Olive green carpet sample"></div>
  <div class="abs prod-info" style="left:236px;top:676px"><b>Northern Birch</b><br>MSRP: $11.69<br>Price: $9.39<br>You Save: $2.30 (20 %)</div>
  <div class="abs prod-info" style="left:380px;top:676px"><b>Northern Birch</b><br>MSRP: $11.69<br>Price: $9.39<br>You Save: $2.30 (20 %)</div>
  <div class="abs prod-info" style="left:525px;top:676px"><b>Northern Birch</b><br>MSRP: $11.69<br>Price: $9.39<br>You Save: $2.30 (20 %)</div>
  <div class="abs add-btn" style="left:236px;top:728px">Add To Cart</div><div class="abs btn-green more-btn" style="left:292px;top:728px">More Info</div>
  <div class="abs add-btn" style="left:379px;top:728px">Add To Cart</div><div class="abs btn-green more-btn" style="left:435px;top:728px">More Info</div>
  <div class="abs add-btn" style="left:525px;top:728px">Add To Cart</div><div class="abs btn-green more-btn" style="left:581px;top:728px">More Info</div>

  <!-- product row 2 -->
  <div class="abs prod-img" style="left:236px;top:770px;background:linear-gradient(135deg,#b73a22,#c8462a,#a8321e)" role="img" aria-label="Red carpet sample"></div>
  <div class="abs prod-img" style="left:380px;top:770px;background:linear-gradient(135deg,#7a4a34,#9c5a3c,#6a4232)" role="img" aria-label="Multicolour brown carpet sample"></div>
  <div class="abs prod-img" style="left:525px;top:770px;background:linear-gradient(135deg,#364d72,#4a5f86,#30456a)" role="img" aria-label="Blue carpet sample"></div>
  <div class="abs prod-info" style="left:236px;top:884px"><b>Northern Birch</b><br>MSRP: $11.69<br>Price: $9.39<br>You Save: $2.30 (20 %)</div>
  <div class="abs prod-info" style="left:380px;top:884px"><b>Northern Birch</b><br>MSRP: $11.69<br>Price: $9.39<br>You Save: $2.30 (20 %)</div>
  <div class="abs prod-info" style="left:525px;top:884px"><b>Northern Birch</b><br>MSRP: $11.69<br>Price: $9.39<br>You Save: $2.30 (20 %)</div>
  <div class="abs add-btn" style="left:234px;top:935px">Add To Cart</div><div class="abs btn-green more-btn" style="left:291px;top:935px">More Info</div>
  <div class="abs add-btn" style="left:378px;top:935px">Add To Cart</div><div class="abs btn-green more-btn" style="left:434px;top:935px">More Info</div>
  <div class="abs add-btn" style="left:523px;top:935px">Add To Cart</div><div class="abs btn-green more-btn" style="left:580px;top:935px">More Info</div>

  <div class="abs btn-green view-more">VIEW MORE PRODUCTS &nbsp;&gt;&gt;</div>

  <footer class="abs footer">
    <div class="abs foot-col" style="left:90px">Home<br>About Us<br>Contact Us</div>
    <div class="abs foot-col" style="left:201px">My Account<br>Shipping Policy<br>Return Policy<br>Privacy Policy<br>Sitemap<br>Cart Help</div>
    <div class="abs foot-col" style="left:301px">Commercial Flooring<br>Carpet Flooring<br>Harwood Flooring<br>Area Rugs</div>
    <div class="abs subscribe">E-Mail Address<div class="abs subscribe-btn">Subscribe</div></div>
    <div class="abs social">
      <span style="background:#2fb4d8"></span>
      <span style="background:#6fb55a"></span>
      <span style="background:#e14a32"></span>
      <span style="background:#c8232c"></span>
    </div>
    <div class="abs copy">© 2014 Company Name ,All Rights Reserved</div>
  </footer>
</body>
</html>
```